New Company Business Card Design

I have a new company logo and I want a new business card design. I dont know if the logo file i attached is in the correct format or quality. We are a New York City Specialty construction Firm specializing in high risk out of the box projects. I want a simple and classy business card that people will his card is as crisp as the work his company does.

Target Market(s)

Clients in the heavy construction industry in New York City

Industry/Entity Type

Construction Company

Contact Information for Business Card

Simple Classy - DIFFERENT

Font styles to use
Other font styles liked:
• Mach the logo font in some way

Colors

Designer to choose colors to be used in the design.

Requirements
Must have
• Uniqueness
Nice to have
• Nothing particular - Just different and classy - Timeless
Should not have
• Goofy Shit or Gimmicky shit

```html
<!DOCTYPE html>
<html lang="en">
<head>
<meta charset="utf-8">
<title>KDR Associates – Business Card</title>
<link rel="stylesheet" href="https://fonts.googleapis.com/css2?family=Fira+Sans:wght@700;800&display=swap">
<style>
  :root {
    --brand-blue: #135fa8;
    --paper: #ffffff;
    --backdrop: #dcdbd8;
    --sky-top: #3f8fcf;
    --sky-bottom: #8ec6e6;
  }
  * { margin: 0; padding: 0; box-sizing: border-box; }
  html, body { width: 1200px; height: 1200px; overflow: hidden; }
  body {
    background: var(--backdrop);
    position: relative;
    font-family: "Fira Sans", Arial, sans-serif;
  }
  .card {
    position: absolute;
    top: 318px;
    width: 307px;
    height: 536px;
    overflow: hidden;
    background: var(--paper);
  }
  .card--front { left: 198px; }
  .card--back { left: 696px; }

  .card__photo {
    position: absolute;
    inset: 0;
    background: linear-gradient(180deg, var(--sky-top) 0%, #5aa6dc 50%, var(--sky-bottom) 100%);
  }
  .wordmark {
    position: absolute;
    font-weight: 800;
    text-transform: uppercase;
    line-height: 1;
    text-align: center;
  }
  .wordmark__name { display: block; letter-spacing: 0.02em; }
  .wordmark__suffix { display: block; letter-spacing: 0.18em; }

  .card--front .wordmark {
    left: 10px;
    top: 16px;
    color: var(--brand-blue);
  }
  .card--front .wordmark__name { font-size: 26px; }
  .card--front .wordmark__suffix { font-size: 5px; margin-top: 2px; }

  .card__band {
    position: absolute;
    left: 0; top: 0;
    width: 100%;
    height: 304px;
    background: var(--brand-blue);
  }
  .card--back .wordmark {
    left: 50%;
    transform: translateX(-50%);
    top: 256px;
    color: var(--paper);
  }
  .card--back .wordmark__name { font-size: 38px; }
  .card--back .wordmark__suffix { font-size: 7px; margin-top: 3px; }

  .name-bar {
    position: absolute;
    left: 0;
    top: 362px;
    width: 187px;
    height: 35px;
    background: var(--brand-blue);
    color: var(--paper);
    font-size: 18px;
    font-weight: 700;
    letter-spacing: 0.03em;
    line-height: 35px;
    padding-left: 23px;
    text-transform: uppercase;
  }
  .contact {
    position: absolute;
    left: 10px;
    top: 412px;
    list-style: none;
    color: var(--brand-blue);
    font-size: 12.5px;
    font-weight: 700;
    line-height: 18.4px;
    letter-spacing: 0.02em;
    text-transform: uppercase;
  }
</style>
</head>
<body>
  <section class="card card--front">
    <div class="card__photo" role="img" aria-label="Photograph of a red lattice crane boom lifting a steel platform with four ironworkers against a blue sky with light clouds"></div>
    <div class="wordmark">
      <span class="wordmark__name">KDR</span>
      <span class="wordmark__suffix">Associates, Inc.</span>
    </div>
  </section>

  <section class="card card--back">
    <div class="card__band"></div>
    <div class="wordmark">
      <span class="wordmark__name">KDR</span>
      <span class="wordmark__suffix">Associates, Inc.</span>
    </div>
    <div class="name-bar">Paul Reyes</div>
    <ul class="contact">
      <li>paulreyes@kdrbuild.com</li>
      <li>412 Pier Rd.</li>
      <li>Linden, NJ 07036</li>
      <li>(908) 555-0148</li>
    </ul>
  </section>
</body>
</html>
```